Cedar Row Maintenance and Concierge Flyer

We need a flyer for cedar row maintenance and concierge service. We specialize in and provide residential maintenance and errand services to retired and semi retired persons living in the Lake Norman area. The services we include:
Lighting and plumbing repairs
Ceiling fan installation
Handicap accessories
Locks and security
Picture hanging
Hang blinds
Furniture arrangement / assembly
Pressure washing
Battery Jump start
and more...

Our Concierge services include:
Errand running
Grocery shopping
Wellness Checks
Dog Walk
Garbage Collection
and more...

We offer monthly service agreements and 24/7 access
Call text or e-mail for more information
704.555.0187
1cedarrowmaint@quillpostmail.com

The design should invoke a sense of trust and a customer service driven mission

Target Market(s)

Residential maintenance

Industry/Entity Type

Property Maintenance

Contact Information for Business Card

Derek Halvorsen
48176 Quimby Ferrel Rd.
Cornelius NC 28031
704.555.0187
with uploaded logo

Requirements
Nice to have
• Would like a postcard size flyer. Front and back
Should not have
• No pics of of people wearing hard hats or pics of blueprints. No pics of commercial or industrial maintenance.

```html
<!DOCTYPE html>
<html lang="en">
<head>
<meta charset="utf-8">
<title>Cedar Row Maintenance and Concierge – Postcard</title>
<link href="https://fonts.googleapis.com/css2?family=Open+Sans:ital,wght@0,400;0,600;0,700;0,800;1,800&display=swap" rel="stylesheet">
<style>
  :root {
    --page: #1b1b1b;
    --red: #d42a2a;
    --band: #d9543a;
    --ink: #2e2e2e;
    --grey: #6b6b6b;
    --panel: #4a4a4a;
    --white: #ffffff;
  }
  * { box-sizing: border-box; margin: 0; padding: 0; }
  html, body { width: 1200px; height: 1200px; overflow: hidden; }
  body {
    background: var(--page);
    font-family: "Open Sans", Arial, sans-serif;
    color: var(--ink);
    position: relative;
  }
  .card {
    position: absolute;
    left: 170px;
    width: 860px;
    height: 557px;
    overflow: hidden;
  }
  .card--front {
    top: 28px;
    background: radial-gradient(ellipse at 30% 20%, #f4f2ec 0%, #dcd9cf 45%, #b9b5a7 100%);
  }
  .card--back { top: 615px; background: var(--white); }

  .brand {
    position: absolute;
    display: flex;
    align-items: center;
    gap: 12px;
  }
  .brand__dot {
    width: 26px; height: 26px; border-radius: 50%;
    background: var(--red); flex: none;
  }
  .brand__name {
    font-weight: 600;
    color: #555;
    line-height: 1.15;
  }
  .card--front .brand { left: 44px; top: 72px; }
  .card--front .brand__name { font-size: 26px; }
  .card--back .brand { left: 48px; top: 462px; }
  .card--back .brand__name { font-size: 16px; }

  .photo { position: absolute; }
  .photo--senior {
    left: 300px; top: 0; width: 560px; height: 557px;
    background:
      radial-gradient(ellipse 30% 40% at 70% 35%, #e9d8c8 0%, rgba(233,216,200,0) 100%),
      radial-gradient(ellipse 55% 45% at 62% 85%, #3a2a2c 0%, rgba(58,42,44,0) 100%),
      linear-gradient(90deg, rgba(185,181,167,0) 0%, #b2ad9f 40%, #a7a294 100%);
  }
  .photo--couple {
    left: 0; top: 150px; width: 330px; height: 390px;
    background: linear-gradient(180deg, rgba(240,232,226,0) 0%, #efe7e2 40%, #f2eeea 75%, rgba(255,255,255,0) 100%);
  }

  .headline {
    position: absolute;
    font-weight: 800;
    color: var(--red);
    letter-spacing: -0.3px;
  }
  .front-intro { position: absolute; left: 49px; top: 222px; width: 250px; }
  .front-intro .headline { position: static; font-size: 29px; line-height: 1.1; }
  .front-intro p { font-size: 19px; line-height: 25px; }
  .front-intro em { font-weight: 800; }

  .band-red {
    position: absolute; left: 0; width: 34px; background: var(--red);
  }
  .card--front .band-red { top: 432px; height: 82px; }
  .card--back .band-red { top: 439px; height: 84px; }

  .offer { position: absolute; left: 52px; top: 434px; }
  .offer__title { font-size: 27px; color: var(--red); line-height: 1.1; }
  .offer__line { font-size: 13.5px; text-transform: uppercase; line-height: 1.5; }
  .offer__big { font-size: 27px; font-weight: 700; color: var(--red); line-height: 1; }

  .contact-band {
    position: absolute; right: 0; background: var(--band); color: var(--white);
    padding-left: 30px; white-space: nowrap;
  }
  .card--front .contact-band { left: 292px; top: 432px; height: 82px; padding-top: 8px; }
  .card--back .contact-band { left: 298px; top: 439px; height: 84px; padding-top: 8px; }
  .contact-band__lead { font-size: 19.5px; line-height: 1.3; }
  .contact-band__row { display: flex; align-items: center; gap: 9px; margin-top: 6px; font-size: 17px; }
  .contact-band__phone { font-weight: 700; font-size: 19px; margin-right: 12px; }
  .contact-band svg { flex: none; }

  .back-intro { position: absolute; left: 40px; top: 42px; width: 230px; }
  .back-intro .headline { position: static; font-size: 31px; line-height: 1.1; }
  .back-intro p { font-size: 16.5px; line-height: 22px; color: #3a3a3a; margin-top: 4px; }

  .service-list { position: absolute; list-style: none; }
  .service-list li {
    display: flex; align-items: center; gap: 14px; font-size: 17px; height: 39.4px; color: #333;
  }
  .service-list svg { width: 26px; height: 26px; flex: none; }
  .service-list .more { color: var(--red); padding-left: 40px; }
  .service-list--main { left: 303px; top: 35px; }
  .service-list--concierge { left: 643px; top: 114px; }
  .service-list--concierge li { height: 41px; }
  .service-list--concierge .more { padding-left: 42px; }

  .concierge-head {
    position: absolute; left: 624px; top: 36px; width: 236px; height: 62px;
    background: var(--panel); border-left: 7px solid var(--red);
    color: var(--white); font-weight: 700; font-size: 19px; line-height: 1.3;
    padding: 4px 0 0 16px; text-transform: uppercase;
  }
</style>
</head>
<body>

<section class="card card--front" aria-label="Postcard front">
  <div class="photo photo--senior" role="img" aria-label="Photo of a thoughtful senior man in glasses and a sweater vest holding a pen"></div>

  <div class="brand">
    <span class="brand__dot"></span>
    <span class="brand__name">Cedar Row<br>Maintenance &amp; Concierge</span>
  </div>

  <div class="front-intro">
    <h1 class="headline">WE SPECIALIZE</h1>
    <p>in and provide residential maintenance and errand services to retired and semi retired persons living in the <em>Lake Norman</em> area.</p>
  </div>

  <div class="band-red"></div>
  <div class="offer">
    <div class="offer__title">WE OFFER</div>
    <div class="offer__line">Monthly service agreements &amp;</div>
    <div class="offer__line"><span class="offer__big">24/7</span> access</div>
  </div>

  <div class="contact-band">
    <div class="contact-band__lead">Call text or e-mail for more information</div>
    <div class="contact-band__row">
      <svg width="22" height="22" viewBox="0 0 22 22"><rect width="22" height="22" rx="4" fill="#fff"/><path d="M7 5c-1 1-1.5 2 0 6s4 6 6 6.5c1 .2 2-.5 2.5-1.3l-2-2-1.3.8c-1-.5-2.5-2.3-3-3.6l1-1.2-1.5-2.5z" fill="#d9543a"/></svg>
      <span class="contact-band__phone">704.555.0187</span>
      <svg width="32" height="21" viewBox="0 0 34 22"><rect x="1" y="1" width="32" height="20" fill="none" stroke="#fff" stroke-width="2"/><path d="M1 1l16 12L33 1M1 21l12-10M33 21L21 11" fill="none" stroke="#fff" stroke-width="2"/></svg>
      <span>1cedarrowmaint@quillpostmail.com</span>
    </div>
  </div>
</section>

<section class="card card--back" aria-label="Postcard back">
  <div class="photo photo--couple" role="img" aria-label="Soft faded photo of a smiling senior couple at a laptop"></div>

  <div class="back-intro">
    <h2 class="headline">OUR SERVICES</h2>
    <p>We offer 5 star services to Lake Norman residents with special attention to retired and semi retired citizens</p>
  </div>

  <ul class="service-list service-list--main">
    <li><svg viewBox="0 0 26 26"><circle cx="13" cy="10" r="7" fill="none" stroke="#d42a2a" stroke-width="2.5"/><rect x="10" y="17" width="6" height="5" fill="#d42a2a"/></svg>Lighting and plumbing repairs</li>
    <li><svg viewBox="0 0 26 26"><path d="M13 13L3 9M13 13l9-9M13 13l3 10" stroke="#d42a2a" stroke-width="2.5"/><circle cx="13" cy="13" r="2.5" fill="#d42a2a"/></svg>Ceiling fan installation</li>
    <li><svg viewBox="0 0 26 26"><circle cx="12" cy="4" r="2.5" fill="#d42a2a"/><path d="M12 8v7h7l3 6" fill="none" stroke="#d42a2a" stroke-width="2.5"/><path d="M8 12a6 6 0 1 0 8 8" fill="none" stroke="#d42a2a" stroke-width="2.5"/></svg>Handicap accessories</li>
    <li><svg viewBox="0 0 26 26"><path d="M8 11V8a5 5 0 0 1 10 0v3" fill="none" stroke="#d42a2a" stroke-width="2.5"/><rect x="6" y="11" width="14" height="12" rx="1" fill="#d42a2a"/></svg>Locks and security</li>
    <li><svg viewBox="0 0 26 26"><rect x="2" y="5" width="22" height="17" fill="none" stroke="#d42a2a" stroke-width="2"/><path d="M8 19l5-7 5 7z" fill="#d42a2a"/></svg>Picture hanging</li>
    <li><svg viewBox="0 0 26 26"><rect x="1" y="4" width="24" height="3" fill="#d42a2a"/><rect x="4" y="7" width="18" height="15" fill="#d42a2a"/></svg>Hang blinds</li>
    <li><svg viewBox="0 0 26 26"><rect x="4" y="8" width="18" height="10" rx="2" fill="#d42a2a"/><rect x="1" y="11" width="5" height="10" rx="1" fill="#d42a2a"/><rect x="20" y="11" width="5" height="10" rx="1" fill="#d42a2a"/></svg>Furniture arrangement / assembly</li>
    <li><svg viewBox="0 0 26 26"><path d="M3 18l3-7h14l3 7v4H3z" fill="#d42a2a"/><circle cx="7" cy="4" r="1.3" fill="#d42a2a"/><circle cx="13" cy="3" r="1.3" fill="#d42a2a"/><circle cx="19" cy="4" r="1.3" fill="#d42a2a"/></svg>Pressure washing</li>
    <li><svg viewBox="0 0 26 26"><rect x="3" y="10" width="18" height="13" fill="#d42a2a"/><path d="M14 10V2" stroke="#d42a2a" stroke-width="2"/></svg>Battery Jump start</li>
    <li class="more">and more...</li>
  </ul>

  <div class="concierge-head">Our concierge<br>services include:</div>

  <ul class="service-list service-list--concierge">
    <li><svg viewBox="0 0 26 26"><circle cx="17" cy="4" r="2.5" fill="#333"/><path d="M5 9l6-2 5 4-3 6 4 4M13 17l-5 3-5-1M16 11l5 2" fill="none" stroke="#333" stroke-width="2.2"/></svg>Errand running</li>
    <li><svg viewBox="0 0 26 26"><path d="M1 7h19l3-5M3 7l3 11h13l2-11" fill="none" stroke="#333" stroke-width="2.2"/><circle cx="8" cy="22" r="1.8" fill="#333"/><circle cx="17" cy="22" r="1.8" fill="#333"/></svg>Grocery shopping</li>
    <li><svg viewBox="0 0 26 26"><path d="M11 2c-4 0-6 3-6 6 0 4 5 6 5 10a3 3 0 0 1-6 0" fill="none" stroke="#333" stroke-width="2"/><circle cx="18" cy="8" r="3" fill="none" stroke="#333" stroke-width="2"/></svg>Wellness Checks</li>
    <li><svg viewBox="0 0 26 26"><ellipse cx="13" cy="18" rx="6" ry="5" fill="#333"/><circle cx="5" cy="11" r="2.8" fill="#333"/><circle cx="10" cy="6" r="2.8" fill="#333"/><circle cx="16" cy="6" r="2.8" fill="#333"/><circle cx="21" cy="11" r="2.8" fill="#333"/></svg>Dog Walk</li>
    <li><svg viewBox="0 0 26 26"><path d="M13 2l3 5c5 2 7 8 6 16H4C3 15 5 9 10 7z" fill="#222"/></svg>Garbage Collection</li>
    <li class="more">and more...</li>
  </ul>

  <div class="band-red"></div>
  <div class="brand">
    <span class="brand__dot"></span>
    <span class="brand__name">Cedar Row<br>Maintenance &amp; Concierge</span>
  </div>

  <div class="contact-band">
    <div class="contact-band__lead">Call text or e-mail for more information</div>
    <div class="contact-band__row">
      <svg width="22" height="22" viewBox="0 0 22 22"><rect width="22" height="22" rx="4" fill="#fff"/><path d="M7 5c-1 1-1.5 2 0 6s4 6 6 6.5c1 .2 2-.5 2.5-1.3l-2-2-1.3.8c-1-.5-2.5-2.3-3-3.6l1-1.2-1.5-2.5z" fill="#d9543a"/></svg>
      <span class="contact-band__phone">704.555.0187</span>
      <svg width="32" height="21" viewBox="0 0 34 22"><rect x="1" y="1" width="32" height="20" fill="none" stroke="#fff" stroke-width="2"/><path d="M1 1l16 12L33 1M1 21l12-10M33 21L21 11" fill="none" stroke="#fff" stroke-width="2"/></svg>
      <span>1cedarrowmaint@quillpostmail.com</span>
    </div>
  </div>
</section>

</body>
</html>
```